Prestige Car Bodyshop Business Card

We are a car bodyshop based in the UK. Our customer base is mainly prestige high-value vehicles. I am looking for a classy and stylish business card design for my staff to give out to customers, with their direct email and phone number, as well as our main email and phone number with address details

I am also looking to have a general business card design with just our main company address and contact details, but also have a space to add a manufacturer approval logo (i.e Velmora, Orek, Tovalo etc... logo) in the corner somewhere.

I do not particularly want any outlines or pictures of cars on the card, I would just like a quality high-end look.

Please feel free to get in touch if you have any questions or queries?

Many Thanks

Malcolm

Target Market(s)

Prestige vehicle owners

Industry/Entity Type

Automotive

Contact Information for Business Card

I am looking for a classy and stylish business card design for my staff to give out to customers, with their direct email and phone number, as well as our main email and phone number with address details

Font styles to use
Sans Serif

Colors

Designer to choose colors to be used in the design.

Requirements
Nice to have
• I do not particularly want any outlines or pictures of cars on the card, I would just like a quality high-end look.

```html
<!DOCTYPE html>
<html lang="en">
<head>
<meta charset="utf-8">
<title>Halden Accident Repair Centre – Business Cards</title>
<link rel="stylesheet" href="https://fonts.googleapis.com/css2?family=Work+Sans:wght@300;400;700&display=swap">
<style>
  :root {
    --bg: #1a1a1a;
    --orange: #ef8427;
    --orange-deep: #cf6a1b;
    --navy: #1f3a78;
    --navy-deep: #173066;
    --blue: #2a5aa8;
    --ink: #2b3b6e;
    --white: #ffffff;
    --circle-light: #e9e9e9;
  }
  * { box-sizing: border-box; margin: 0; padding: 0; }
  html, body {
    width: 1200px; height: 963px; overflow: hidden;
    background: var(--bg);
    font-family: "Work Sans", Arial, sans-serif;
  }
  .sheet {
    width: 1200px; height: 963px;
    display: flex; flex-direction: column;
    align-items: center; justify-content: center; gap: 70px;
  }
  .card {
    position: relative;
    width: 600px; height: 343px;
    border-radius: 16px;
    overflow: hidden;
  }
  /* Front */
  .card--front { background: var(--white); }
  .card__wave { position: absolute; inset: 0; width: 100%; height: 100%; }
  .brand {
    position: absolute; display: flex; align-items: center;
  }
  .brand__mark {
    width: 78px; height: 78px; border-radius: 50%; flex: none;
  }
  .brand__text { margin-left: 10px; }
  .brand__name {
    font-weight: 300; font-size: 40px; letter-spacing: 1px; line-height: 1;
  }
  .brand__rule { height: 1.5px; margin: 6px 0 4px; }
  .brand__tag {
    font-weight: 300; font-size: 11.5px; letter-spacing: 0.6px; text-transform: uppercase;
  }
  .card--front .brand { left: 34px; top: 70px; }
  .card--front .brand__mark { background: radial-gradient(circle at 35% 30%, var(--blue), var(--navy-deep)); }
  .card--front .brand__name,
  .card--front .brand__tag { color: var(--navy); }
  .card--front .brand__rule { background: var(--navy); }

  .divider {
    position: absolute; left: 318px; top: 112px;
    width: 1.5px; height: 140px; background: var(--navy);
  }
  .contact {
    position: absolute; left: 342px; top: 112px;
    color: var(--ink); font-size: 13px; line-height: 1.4;
  }
  .contact__name {
    color: var(--orange); font-weight: 700; font-size: 21px; letter-spacing: 0.5px;
    text-transform: uppercase; line-height: 1.1;
  }
  .contact__role { margin-bottom: 6px; }
  .contact__address { margin-bottom: 6px; }
  .contact__row { display: flex; align-items: center; gap: 7px; }
  .contact__icon { width: 10px; height: 10px; flex: none; }

  /* Back */
  .card--back {
    background: linear-gradient(160deg, var(--orange-deep) 0%, var(--orange) 55%, var(--orange-deep) 100%);
  }
  .card--back .brand { left: 50%; top: 50%; transform: translate(-50%, -50%); }
  .card--back .brand__mark { width: 100px; height: 100px; background: var(--circle-light); }
  .card--back .brand__text { margin-left: 14px; }
  .card--back .brand__name { font-size: 50px; color: var(--white); }
  .card--back .brand__rule { background: var(--white); }
  .card--back .brand__tag { font-size: 14px; color: var(--white); }
</style>
</head>
<body>
<main class="sheet">

  <section class="card card--front" aria-label="Business card front">
    <svg class="card__wave" viewBox="0 0 600 343" preserveAspectRatio="none" aria-hidden="true">
      <defs>
        <linearGradient id="waveBlue" x1="0" y1="0" x2="1" y2="1">
          <stop offset="0" stop-color="#2a5aa8"/>
          <stop offset="1" stop-color="#173066"/>
        </linearGradient>
      </defs>
      <path d="M0,182 C110,230 250,250 420,343 L0,343 Z" fill="url(#waveBlue)"/>
      <path d="M0,170 C120,215 270,238 440,343" fill="none" stroke="#ef8427" stroke-width="3"/>
    </svg>

    <div class="brand">
      <div class="brand__mark"></div>
      <div class="brand__text">
        <div class="brand__name">HALDEN</div>
        <div class="brand__rule"></div>
        <div class="brand__tag">Accident Repair Centre</div>
      </div>
    </div>

    <div class="divider"></div>

    <div class="contact">
      <div class="contact__name">Tomas Reyne</div>
      <div class="contact__role">Director</div>
      <div class="contact__address">48 Harrow Mill Road,<br>Kestwick KW4 7PL</div>
      <div class="contact__row">
        <svg class="contact__icon" viewBox="0 0 10 10" aria-hidden="true"><path d="M2,0.5 L3.6,0.5 L4.2,2.8 L3,3.6 C3.6,5 4.9,6.3 6.4,7 L7.2,5.8 L9.5,6.4 L9.5,8 C9.5,9 8.8,9.5 8,9.5 C3.8,9.2 0.8,6.2 0.5,2 C0.5,1.2 1,0.5 2,0.5 Z" fill="#ef8427"/></svg>
        <span>0161 555 0142</span>
      </div>
      <div class="contact__row">
        <svg class="contact__icon" viewBox="0 0 10 10" aria-hidden="true"><rect x="0.5" y="2" width="9" height="6.5" fill="none" stroke="#ef8427" stroke-width="1.2"/><path d="M0.5,2 L5,5.6 L9.5,2" fill="none" stroke="#ef8427" stroke-width="1.2"/></svg>
        <span>info@haldenrepair.co.uk</span>
      </div>
      <div class="contact__row">
        <svg class="contact__icon" viewBox="0 0 10 10" aria-hidden="true"><circle cx="5" cy="5" r="4.3" fill="none" stroke="#ef8427" stroke-width="1.1"/><ellipse cx="5" cy="5" rx="1.8" ry="4.3" fill="none" stroke="#ef8427" stroke-width="1"/><path d="M0.7,5 H9.3" stroke="#ef8427" stroke-width="1"/></svg>
        <span>www.haldenrepair.co.uk</span>
      </div>
    </div>
  </section>

  <section class="card card--back" aria-label="Business card back">
    <div class="brand">
      <div class="brand__mark"></div>
      <div class="brand__text">
        <div class="brand__name">HALDEN</div>
        <div class="brand__rule"></div>
        <div class="brand__tag">Accident Repair Centre</div>
      </div>
    </div>
  </section>

</main>
</body>
</html>
```